VELOMIRA needs a label design for their product line of therapeutic CBD HEMP oil.

We are a company based out of Hawaii, USA called "VeloMira". We are needing a new look for our labels on our 2 oz bottles of CBD hemp oil. We are using organic CBD rich hemp oil and combining it with other organic oils to help heal inflammation, skin problems, and other ailments.

We have 6 different products of CBD oils :
x 2 CBD oil tinctures ( internal) : ZENITH CBD and BOTANIQ FORMULA
x 3 CBD skin care oils (external): CBD FACIAL SOLSTICE, CBD BODY
OIL, and CBD SKIN CARE
x 1 CBD Therapeutic oil ( external) SOOTHAVEX - Inflammation
Each product is in a 2 oz amber bottle with a black mist sprayer cap or black dropper and is a different color label. A green bottle ( zenith cbd), blue (botaniq), yellow(body oil), red/pink (restorative), purple( soothavex) the other colors???
I would like to use the color gold in our labels.

There is the logo for the name 'VeloMira", an oil droplet, and hemp leaf on each bottle.
I have the descriptive text/layout for the wording to be placed on the side of the bottles which just need a little font finessing.
I have designed the labels but just cannot seem to make them look professional and would like to re create the look.

I am seeking a label that looks professional for a successful business of high quality oils.

Target Market(s)

health food stores, alternative medicines, internet,

Industry/Entity Type

Graphic Design

Requirements
Must have
• I would like the word or logo for organic on the bottle.
• There must be a small space left for the bar code.
• I would like them all to look similar just with different colors and a slight different layout to distinguish the 2 internal CBD tiinctures ( CBD ZENTIH, BOTANIQ FORMULA) + soothavex from the 3 skin care external skin oils.
Nice to have
• I would like my product to have a hemp leaf somewhere on it but not too obvious.
• I am more concerned with the front design of the bottles than the written words on the sides of the bottle. That could be worked on later.
Should not have
• my label should not look too busy!

```html
<!DOCTYPE html>
<html lang="en">
<head>
<meta charset="utf-8">
<title>VeloMira CBD Labels</title>
<link href="https://fonts.googleapis.com/css2?family=Arimo:wght@400;700&display=swap" rel="stylesheet">
<style>
  :root {
    --page-bg: #e9e9e9;
    --label-bg: #ffffff;
    --gold: #d9a71c;
    --ink: #2f2f2f;
    --leaf-green: #4f8a2a;
    --blue: #1268b3;
    --blue-deep: #0a4e9c;
    --purple: #8c2a8c;
    --purple-deep: #7a1f86;
    --green: #3aaa35;
    --green-deep: #2f9a2c;
  }
  * { box-sizing: border-box; margin: 0; padding: 0; }
  html, body { width: 900px; height: 1200px; overflow: hidden; }
  body {
    background: var(--page-bg);
    font-family: "Arimo", Arial, sans-serif;
    display: flex;
    align-items: center;
    justify-content: center;
    gap: 40px;
  }
  .label {
    position: relative;
    width: 250px;
    height: 300px;
    background: var(--label-bg);
    border-top: 4px solid var(--gold);
    box-shadow: 0 2px 10px rgba(0,0,0,0.12);
    overflow: hidden;
    text-align: center;
  }
  .label--blue { --accent: var(--blue); --accent-deep: var(--blue-deep); }
  .label--purple { --accent: var(--purple); --accent-deep: var(--purple-deep); }
  .label--green { --accent: var(--green); --accent-deep: var(--green-deep); }

  .hemp-leaf {
    position: absolute;
    top: 0;
    left: 8px;
    width: 96px;
    height: 62px;
    background: linear-gradient(180deg, var(--leaf-green), #7fb445);
    border-radius: 0 0 48px 48px;
  }
  .spec {
    position: absolute;
    top: 26px;
    right: 14px;
    font-size: 10px;
    line-height: 14px;
    color: var(--accent);
    text-align: right;
  }
  .brand {
    position: absolute;
    top: 74px;
    left: 0;
    right: 0;
    display: flex;
    flex-direction: column;
    align-items: center;
    gap: 4px;
  }
  .brand__dot {
    width: 12px;
    height: 12px;
    border-radius: 50%;
    background: var(--gold);
  }
  .brand__name {
    font-size: 22px;
    font-weight: 400;
    color: var(--ink);
  }
  .title {
    position: absolute;
    top: 130px;
    left: 0;
    right: 0;
    font-size: 26px;
    font-weight: 700;
    line-height: 29px;
    color: var(--accent);
  }
  .subtitle {
    position: absolute;
    top: 168px;
    left: 0;
    right: 0;
    font-size: 11px;
    font-weight: 700;
    line-height: 14px;
    color: var(--accent);
  }
  .title--two-line + .subtitle { display: none; }
  .faint-leaf {
    position: absolute;
    left: 60px;
    bottom: 40px;
    width: 130px;
    height: 60px;
    background: var(--accent);
    opacity: 0.08;
    border-radius: 65px 65px 0 0;
  }
  .base-band {
    position: absolute;
    left: 0;
    right: 0;
    bottom: 0;
    height: 58px;
    background: linear-gradient(90deg, var(--accent-deep), var(--accent));
    clip-path: polygon(0 45%, 20% 25%, 40% 40%, 60% 10%, 80% 30%, 100% 0, 100% 100%, 0 100%);
  }
  .volume {
    position: absolute;
    left: 0;
    right: 0;
    bottom: 18px;
    font-size: 10px;
    color: #ffffff;
    padding-left: 30px;
  }
</style>
</head>
<body>

  <section class="label label--blue">
    <div class="hemp-leaf" role="img" aria-label="Green hemp leaf illustration"></div>
    <p class="spec">500mg Cannabidiol<br>150mg β - Caryophyllene</p>
    <div class="brand"><span class="brand__dot"></span><span class="brand__name">VeloMira</span></div>
    <h2 class="title title--two-line">BOTANIQ<br>FORMULA</h2>
    <p class="subtitle"></p>
    <div class="faint-leaf" role="img" aria-label="Faint hemp leaf watermark"></div>
    <div class="base-band" role="img" aria-label="Blue hemp leaf silhouette"></div>
    <p class="volume">1 Fl Oz. / 30ml Dietary Supplement</p>
  </section>

  <section class="label label--purple">
    <div class="hemp-leaf" role="img" aria-label="Green hemp leaf illustration"></div>
    <p class="spec">CBD Rich Hemp Oil &amp;<br>BCP Rich Copaiba Oil</p>
    <div class="brand"><span class="brand__dot"></span><span class="brand__name">VeloMira</span></div>
    <h2 class="title">SOOTHAVEX</h2>
    <p class="subtitle">Pure, Natural Organic Oils</p>
    <div class="faint-leaf" role="img" aria-label="Faint hemp leaf watermark"></div>
    <div class="base-band" role="img" aria-label="Purple hemp leaf silhouette"></div>
    <p class="volume">2 Fl Oz. / 30ml</p>
  </section>

  <section class="label label--green">
    <div class="hemp-leaf" role="img" aria-label="Green hemp leaf illustration"></div>
    <p class="spec">500mg Cannabidiol</p>
    <div class="brand"><span class="brand__dot"></span><span class="brand__name">VeloMira</span></div>
    <h2 class="title">CBD ZENITH</h2>
    <p class="subtitle">CBD Rich Hemp Oil<br>Organic CO₂ Extract</p>
    <div class="faint-leaf" role="img" aria-label="Faint hemp leaf watermark"></div>
    <div class="base-band" role="img" aria-label="Green hemp leaf silhouette"></div>
    <p class="volume">1 Fl Oz. / 30ml Dietary Supplement</p>
  </section>

</body>
</html>
```